Life Coach for Lawyers Business Card Design

Elegant, original, business card design for life coaching service for associate attorneys who work in big law and struggle with stress, overwhelm, and time management. Double sided design.

Target Market(s)

Women associate attorneys who work in big law and struggle with stress, overwhelm, and time management.

Industry/Entity Type

Life Coaching

Contact Information for Business Card

Marlene Quorthby
Life Coach
519.607.4431
brightcounselpath.net
marlene@brightcounselpath.net
@brightcounselpath (Instagram)

Font styles to use
Other font styles liked:
• Silver South font duo. See uploaded files.

Requirements
Must have
• Icons for phone, website, email, and Instagram instead of words. Specific colors used in my logo (171B2B, 421121, FFFFFF)
Nice to have
• Foil. Embossed. Feminine design.
Should not have
• Any colors other than those used in logo. See uploaded files.

```html
<!DOCTYPE html>
<html lang="en">
<head>
<meta charset="utf-8">
<title>Bright Counsel Path – Business Card</title>
<link rel="stylesheet" href="https://fonts.googleapis.com/css2?family=Playfair+Display:wght@500;600&family=Open+Sans:wght@400;600&display=swap">
<style>
  :root {
    --navy: #171B2B;
    --wine: #421121;
    --wine-deep: #3a1020;
    --white: #FFFFFF;
    --paper: #f4f4f4;
    --backdrop: #d9d9d9;
  }
  * { box-sizing: border-box; margin: 0; padding: 0; }
  html, body { width: 1200px; height: 1021px; overflow: hidden; }
  body {
    background: var(--backdrop);
    display: flex;
    flex-direction: column;
    align-items: center;
    justify-content: center;
    gap: 44px;
    font-family: "Open Sans", sans-serif;
  }
  .card {
    width: 760px;
    height: 434px;
    position: relative;
    box-shadow: 0 6px 18px rgba(0,0,0,0.18);
  }

  /* Back side */
  .card-back {
    background: var(--wine-deep);
    display: flex;
    align-items: center;
    justify-content: center;
  }
  .seal {
    display: flex;
    align-items: center;
    gap: 18px;
  }
  .seal-circle {
    width: 22px; height: 22px;
    border-radius: 50%;
    background: var(--white);
  }
  .seal-name {
    font-family: "Playfair Display", serif;
    font-weight: 500;
    font-size: 34px;
    letter-spacing: 6px;
    color: var(--white);
    text-transform: uppercase;
  }

  /* Front side */
  .card-front {
    background: var(--paper);
    color: var(--navy);
  }
  .brand-name {
    position: absolute;
    top: 96px;
    left: 0; right: 0;
    text-align: center;
    padding-left: 110px;
    font-family: "Playfair Display", serif;
    font-weight: 600;
    font-size: 50px;
    letter-spacing: 3px;
    color: var(--wine);
    text-transform: uppercase;
  }
  .details {
    position: absolute;
    top: 238px;
    left: 70px;
    display: flex;
    align-items: stretch;
  }
  .identity {
    text-align: right;
    padding-right: 24px;
    padding-top: 8px;
  }
  .person-name {
    font-family: "Playfair Display", serif;
    font-weight: 600;
    font-size: 22px;
    letter-spacing: 1px;
    color: var(--wine);
    text-transform: uppercase;
  }
  .person-role {
    font-size: 18px;
    color: var(--navy);
    margin-top: 2px;
  }
  .divider {
    width: 1.5px;
    background: var(--navy);
    margin-right: 18px;
  }
  .contact-list { list-style: none; }
  .contact-item {
    display: flex;
    align-items: center;
    gap: 10px;
    font-size: 20px;
    line-height: 30px;
    color: var(--navy);
  }
  .contact-icon {
    width: 18px; height: 18px;
    flex: none;
  }
  .contact-dot {
    width: 14px; height: 14px;
    margin: 0 2px;
    border-radius: 50%;
    background: var(--wine);
    flex: none;
  }
</style>
</head>
<body>

  <section class="card card-back" aria-label="Card back">
    <div class="seal">
      <span class="seal-circle"></span>
      <span class="seal-name">Bright Counsel Path</span>
    </div>
  </section>

  <section class="card card-front" aria-label="Card front">
    <div class="brand-name">Bright Counsel Path</div>

    <div class="details">
      <div class="identity">
        <div class="person-name">Marlene Quorthby</div>
        <div class="person-role">Life Coach</div>
      </div>
      <div class="divider"></div>
      <ul class="contact-list">
        <li class="contact-item">
          <svg class="contact-icon" viewBox="0 0 24 24" aria-hidden="true">
            <path fill="var(--wine)" d="M6.6 10.8a15.2 15.2 0 0 0 6.6 6.6l2.2-2.2a1 1 0 0 1 1-.25 11.4 11.4 0 0 0 3.6.57 1 1 0 0 1 1 1V20a1 1 0 0 1-1 1A17 17 0 0 1 3 4a1 1 0 0 1 1-1h3.5a1 1 0 0 1 1 1c0 1.25.2 2.45.57 3.57a1 1 0 0 1-.25 1z"/>
          </svg>
          519.607.4431
        </li>
        <li class="contact-item">
          <svg class="contact-icon" viewBox="0 0 24 24" aria-hidden="true">
            <rect x="2.5" y="5" width="19" height="14" fill="none" stroke="var(--wine)" stroke-width="2"/>
            <path d="M3 6l9 7 9-7" fill="none" stroke="var(--wine)" stroke-width="2"/>
          </svg>
          brightcounselpath.net
        </li>
        <li class="contact-item">
          <svg class="contact-icon" viewBox="0 0 24 24" aria-hidden="true">
            <circle cx="12" cy="12" r="9.5" fill="none" stroke="var(--wine)" stroke-width="2"/>
            <ellipse cx="12" cy="12" rx="4" ry="9.5" fill="none" stroke="var(--wine)" stroke-width="1.6"/>
            <path d="M2.5 12h19M4 7.5h16M4 16.5h16" stroke="var(--wine)" stroke-width="1.4"/>
          </svg>
          marlene@brightcounselpath.net
        </li>
        <li class="contact-item">
          <span class="contact-dot"></span>
          @brightcounselpath
        </li>
      </ul>
    </div>
  </section>

</body>
</html>
```